Dale Morrikan Plumbing and Heating

Need a card design for a plumbing and heating company that does service and repair, remodels, and plumbing in new construction. Please add following on back side of card; Boilers, Water heaters, Gas lines, Sump pumps, Toilet repairs, Faucet repairs, Pipe thawing, Radiant heating, New construction, Remodels.

Industry/Entity Type

Plumber

Contact Information for Business Card

Was thinking white gloss card with colored logo in middle or black glossy card with silver logo in middle. Just a thought but very open to other designs.

Requirements
Must have
• Need following on front of card;
• P(203) 321-8689
• C(203) 232-9069
• Dale Morrikan 275 Larkwell St West, Stamford, Ct 06214
• service@DrainHearth.example (plumbing in blue, heating in red)
• www.DrainHearth.example (plumbing in blue, heating in red)
• Fully Licensed and Insured
Nice to have
• Elegant design

```html
<!DOCTYPE html>
<html lang="en">
<head>
<meta charset="utf-8">
<title>Dale Morrikan Plumbing and Heating – Business Card</title>
<link rel="stylesheet" href="https://fonts.googleapis.com/css2?family=Open+Sans:wght@400;600;700&display=swap">
<style>
  :root {
    --backdrop: #e9e6e1;
    --card-white: #ffffff;
    --card-black: #0b0b0c;
    --ink: #1d1d1f;
    --brand-blue: #2d5fb8;
    --brand-red: #d8394a;
    --silver: #c9ced6;
    --text-light: #f2f2f2;
  }
  * { box-sizing: border-box; margin: 0; padding: 0; }
  html, body { width: 1200px; height: 913px; overflow: hidden; }
  body {
    background: var(--backdrop);
    font-family: "Open Sans", Arial, sans-serif;
    position: relative;
  }
  .card {
    position: absolute;
    width: 540px;
    height: 309px;
    border-radius: 16px;
    overflow: hidden;
    box-shadow: 0 10px 28px rgba(0,0,0,.22);
  }
  .card-front { left: 40px; top: 302px; background: var(--card-white); }
  .card-back  { left: 620px; top: 302px; background: var(--card-black); }

  .front-shape { position: absolute; inset: 0; }

  .contact-block { position: absolute; left: 34px; top: 108px; color: var(--ink); }
  .person-name { font-size: 22px; font-weight: 700; letter-spacing: .5px; line-height: 1; }
  .person-role { font-size: 12px; font-weight: 700; color: var(--brand-blue); margin-top: 3px; letter-spacing: .5px; }
  .address { font-size: 12.5px; margin-top: 14px; line-height: 1.35; }
  .contact-list { list-style: none; margin-top: 8px; }
  .contact-list li { display: flex; align-items: center; gap: 8px; font-size: 12.5px; font-weight: 600; line-height: 1.5; }
  .contact-list svg { width: 11px; height: 11px; fill: var(--brand-blue); flex: none; }
  .blue { color: var(--brand-blue); }
  .red { color: var(--brand-red); }

  .brand { text-align: center; color: var(--silver); }
  .brand-mark { display: inline-block; width: 14px; height: 14px; border-radius: 50%; background: var(--brand-blue); margin-bottom: 6px; }
  .brand-name { font-weight: 700; font-size: 19px; letter-spacing: 1px; text-transform: uppercase; line-height: 1.15; }
  .brand-web { font-size: 9px; color: var(--silver); margin-top: 3px; letter-spacing: .5px; }

  .front-brand { position: absolute; right: 30px; top: 70px; width: 220px; }
  .licensed { position: absolute; right: 34px; top: 176px; color: var(--text-light); font-size: 13px; font-weight: 600; }

  .back-brand { position: absolute; left: 0; right: 0; top: 42px; }
  .service-list {
    position: absolute; left: 110px; top: 160px;
    list-style: none;
    columns: 2; column-gap: 40px;
    color: var(--text-light);
    font-size: 13px;
  }
  .service-list li { display: flex; align-items: center; gap: 9px; line-height: 1.45; }
  .service-list li::before {
    content: ""; width: 9px; height: 9px; border-radius: 50%;
    background: var(--brand-blue); flex: none;
  }
</style>
</head>
<body>

  <section class="card card-front" aria-label="Business card front">
    <svg class="front-shape" viewBox="0 0 540 309" preserveAspectRatio="none" aria-hidden="true">
      <path d="M300,0 C225,95 250,255 370,309 L540,309 L540,0 Z" fill="var(--card-black)"/>
      <path d="M294,0 C219,95 244,255 362,309" fill="none" stroke="var(--brand-blue)" stroke-width="3"/>
    </svg>

    <div class="brand front-brand">
      <span class="brand-mark"></span>
      <div class="brand-name">Dale Morrikan<br>Plumbing and Heating</div>
      <div class="brand-web">www.DrainHearth.example</div>
    </div>
    <p class="licensed">Fully Licensed and Insured</p>

    <div class="contact-block">
      <h1 class="person-name">EVAN HOLT</h1>
      <p class="person-role">OWNER</p>
      <p class="address">Dale Morrikan 275 Larkwell<br>St West, Stamford, Ct 06214</p>
      <ul class="contact-list">
        <li><svg viewBox="0 0 24 24"><path d="M6.6 10.8a15 15 0 0 0 6.6 6.6l2.2-2.2a1 1 0 0 1 1-.25 11.4 11.4 0 0 0 3.6.57 1 1 0 0 1 1 1V20a1 1 0 0 1-1 1A17 17 0 0 1 3 4a1 1 0 0 1 1-1h3.5a1 1 0 0 1 1 1c0 1.25.2 2.45.57 3.57a1 1 0 0 1-.25 1z"/></svg>(203) 555-0147</li>
        <li><svg viewBox="0 0 24 24"><path d="M7 1h10a2 2 0 0 1 2 2v18a2 2 0 0 1-2 2H7a2 2 0 0 1-2-2V3a2 2 0 0 1 2-2zm0 3v14h10V4z"/></svg>(203) 555-0183</li>
        <li><svg viewBox="0 0 24 24"><path d="M2 4h20v16H2zm2 2v.5l8 5 8-5V6zm0 3v9h16V9l-8 5z"/></svg>service@<span class="blue">Drain</span><span class="red">Hearth</span>.example</li>
        <li><svg viewBox="0 0 24 24"><circle cx="12" cy="12" r="10"/></svg>www.<span class="blue">Drain</span><span class="red">Hearth</span>.example</li>
      </ul>
    </div>
  </section>

  <section class="card card-back" aria-label="Business card back">
    <div class="brand back-brand">
      <span class="brand-mark"></span>
      <div class="brand-name">Dale Morrikan<br>Plumbing and Heating</div>
      <div class="brand-web">www.DrainHearth.example</div>
    </div>
    <ul class="service-list">
      <li>Boilers</li>
      <li>Water heaters</li>
      <li>Gas lines</li>
      <li>Sump pumps</li>
      <li>Toilet repairs</li>
      <li>Faucet repairs</li>
      <li>Pipe thawing</li>
      <li>Radiant heating</li>
      <li>New construction</li>
      <li>Remodels</li>
    </ul>
  </section>

</body>
</html>
```